Brochure Design Project

Our company is TEM Bexley Fold. (no LOGO)

We are a restaurant marketing and advertising service. We market restaurants menus by producing a menu guide, distributing flyers and post cards, and also placing the restaurants menu on our website for delivery.

We make restaurants more profitable, by making their food more accessible. Marketing restaurants on search engines, websites, friendloop, vrop, zindle, and a total of 21 different marketing techniques that make restaurants more money.

Key Point: This is all done at NO COST to the restaurant.

We are looking for a design for a brochure that will be mailed as well as handed to restaurateurs.

In my attached file I am including our sales letter. The letter can stay in letter form for the inside of a tri-fold brochure or it can be part of your design.

For more information about our service, please read the attached sales letter.

Target Market(s)

Restaurant Owners and General managers

Industry/Entity Type

Advertising

Requirements
Must have
• Must look attractive and Eye-catching

```html
<!DOCTYPE html>
<html lang="en">
<head>
<meta charset="utf-8">
<title>TEM Bexley Fold – Restaurant Marketing Brochure</title>
<link rel="stylesheet" href="https://fonts.googleapis.com/css2?family=Archivo+Black&family=Roboto+Condensed:ital,wght@1,700&family=Open+Sans:wght@400;600;700&display=swap">
<style>
  :root {
    --backdrop: #667070;
    --brand-red: #b0121b;
    --ink: #141414;
    --paper: #ffffff;
    --cream: #f1ebdc;
    --cream-text: #f6ecd8;
    --photo-light: #eef0f1;
    --photo-mid: #c9cdd0;
    --label: #ffffff;
  }
  * { box-sizing: border-box; margin: 0; padding: 0; }
  html, body { width: 1200px; height: 900px; overflow: hidden; }
  body {
    background: var(--backdrop);
    font-family: "Open Sans", Arial, sans-serif;
    position: relative;
  }
  .panel-label {
    position: absolute; top: 196px;
    color: var(--label); font-size: 13px;
  }
  .panel {
    position: absolute; top: 232px; width: 255px; height: 400px;
    overflow: hidden; background: var(--paper);
  }

  /* Front cover */
  .front { left: 60px; }
  .front .question-band {
    height: 86px; background: var(--brand-red);
    display: flex; align-items: center; justify-content: center;
    padding: 0 18px; text-align: center;
    font-family: "Roboto Condensed", "Arial Narrow", sans-serif;
    font-style: italic; font-weight: 700; font-size: 12.5px; line-height: 1.15;
    color: var(--paper); text-transform: uppercase;
  }
  .front .cover-photo {
    position: absolute; top: 86px; left: 0; right: 0; bottom: 0;
    background: linear-gradient(160deg, var(--photo-light) 0%, var(--photo-mid) 100%);
  }
  .front .cover-headline {
    position: absolute; top: 140px; left: 14px; width: 170px;
    font-family: "Archivo Black", Impact, sans-serif;
    font-size: 17px; line-height: 1.02; color: var(--ink);
    text-transform: uppercase;
  }

  /* Inside spread */
  .inside-left { left: 350px; }
  .inside-left .answer-band {
    height: 168px; background: var(--brand-red);
    padding: 14px 18px; color: var(--cream-text);
    font-family: "Archivo Black", Impact, sans-serif;
  }
  .answer-band .lead { font-size: 12px; line-height: 1; }
  .answer-band .yes { font-size: 58px; line-height: 0.9; }
  .answer-band .follow { font-size: 14px; line-height: 1.05; margin-top: 4px; }
  .inside-left .body-copy {
    background: linear-gradient(180deg, var(--photo-light), #d8dbdd);
    height: 232px; padding: 16px 18px;
  }
  .body-copy p {
    font-size: 7.4px; line-height: 1.45; color: #2a2a2a; margin-bottom: 8px;
  }

  .inside-right { left: 605px; background: var(--cream); padding: 22px 20px; }
  .guarantee {
    font-family: "Archivo Black", Impact, sans-serif; text-transform: uppercase;
    line-height: 0.85; margin-bottom: 14px;
  }
  .guarantee .we, .guarantee .it { color: var(--brand-red); font-size: 54px; display: block; }
  .guarantee .word { color: var(--ink); font-size: 27px; display: block; margin: -8px 0 -6px; }
  .inside-right .subhead {
    font-weight: 700; font-size: 9px; color: var(--ink); margin-bottom: 16px;
  }
  .inside-right p { font-size: 7.4px; line-height: 1.5; color: #2a2a2a; margin-bottom: 8px; }
  .inside-right .no-cost { color: var(--brand-red); font-weight: 700; }
  .inside-right .signoff { font-weight: 700; }

  /* Back cover */
  .back { left: 895px; }
  .back .identity { position: absolute; top: 168px; left: 0; right: 0; text-align: center; }
  .back .company-name { color: var(--brand-red); font-weight: 600; font-size: 19px; }
  .back .address { font-size: 7px; color: #444; margin-top: 3px; }
  .back .footer-band {
    position: absolute; left: 0; right: 0; bottom: 0; height: 8px; background: var(--brand-red);
  }
</style>
</head>
<body>
  <span class="panel-label" style="left:60px">Front</span>
  <span class="panel-label" style="left:350px">Inside</span>
  <span class="panel-label" style="left:895px">Back</span>

  <section class="panel front">
    <div class="question-band">Would a check for $18,375 with your restaurants name on it be worth a 15 minute conversation?</div>
    <div class="cover-photo" role="img" aria-label="Photo of a waiter in a dark suit and white glove holding a silver serving tray, towel over the arm"></div>
    <h1 class="cover-headline">Are you tired of ineffective marketing and advertising?</h1>
  </section>

  <section class="panel inside-left">
    <div class="answer-band">
      <div class="lead">If you answered</div>
      <div class="yes">yes</div>
      <div class="follow">to either question, we should talk about our all-inclusive marketing plan.</div>
    </div>
    <div class="body-copy">
      <p>Our marketing plan places your menu in front of thousands of customers each and every month. Hungry customers looking to buy immediately. Hungry customers that want food now. The more people see your menu, the more likely a customer will purchase food from your restaurant.</p>
      <p>Ever have a problem with down time at your restaurant? Customers are not dining in or taking out because it's too hot or too cold or it's raining outside? That's a problem that you wouldn't have to have, if you made your food more accessible.</p>
      <p>TEM Bexley Fold is a full service restaurant marketing and advertising service that specializes in delivery. We deliver food from a variety of restaurants to people at their homes, offices and hotels! Using our marketing plan we will bring more exposure to your restaurant and increase your bottom line.</p>
    </div>
  </section>

  <section class="panel inside-right">
    <h2 class="guarantee"><span class="we">We</span><span class="word">Guarantee</span><span class="it">It!</span></h2>
    <div class="subhead">How many marketers and advertisers say that?</div>
    <p>We do! We guarantee that you will only make money and not pay money. There are never any participation cost, or fees associated with our service. We use a combination of 21 proven Marketing techniques to drive your profits up while keeping cost down.</p>
    <p>So what should you do? Call me now at 555-0142 to schedule a 15 min consultation that is guaranteed to <span class="no-cost">NOT COST</span> you anything and only make your restaurant money.</p>
    <p>Talk to you soon!</p>
    <p class="signoff">Sam Halvey · 555-0142 (cell) · tembexleyfold.example</p>
    <p>p.s.<br>I have a check with your restaurants name on it, so contact me before July 26, 2013! You can also schedule an appointment online at tembexleyfold.example</p>
  </section>

  <section class="panel back">
    <div class="identity">
      <div class="company-name">TEM Bexley Fold</div>
      <div class="address">14 Corran Street, Bexley Fold</div>
    </div>
    <div class="footer-band"></div>
  </section>
</body>
</html>
```